MossVane Spa, Skincare and Cosmetics website

I need a website for MossVane (putting the glow back into people's skin) which allows viewers to access information about Beauty Spa packaging and facilities as well as online skincare and cosmetic products. Our distinctive difference is that our products are certified organic. We want to target a luxury high income niche market (age 30-50). I want all colours to be "baby colours" preferably background to be "baby metallic pink" (but please don't make the website too immature) with curves as patterns. I want a romantic vintage look.

The website needs to look:
1. elegant (prestige and luxury)
2. bright (baby colours mainly)
3. European curves and signature patterns
4. Can include Pearl related pics (but not a must)

The website pages needs to have:
1. pages ordering skincare/cosmetics
2. shopping cart and payment
3. about us and about our product differences
4. contact us
5. booking for spa treatments and packages

I have attached our logo and also packaging label styles.

Industry/Entity Type

Cosmetics

```html
<!DOCTYPE html>
<html lang="en">
<head>
<meta charset="utf-8">
<title>MossVane Spa, Skincare and Cosmetics</title>
<link rel="stylesheet" href="https://fonts.googleapis.com/css2?family=Open+Sans:wght@400;600;700&family=Oswald:wght@300;400&family=Courgette&display=swap">
<style>
  :root {
    --rose: #e25b7e;
    --rose-deep: #d2436a;
    --rose-dark: #a4304f;
    --peach: #fdc9b6;
    --blush: #f9d7de;
    --blush-light: #fdeef1;
    --wine: #8c1d3c;
    --red: #d8383f;
    --hex-red: #c9343e;
    --ink: #222222;
    --muted: #555555;
    --white: #ffffff;
    --footer: #1f1f1f;
    --footer-text: #b9b9b9;
  }
  * { box-sizing: border-box; margin: 0; padding: 0; }
  html, body { width: 675px; height: 1200px; overflow: hidden; }
  body {
    position: relative;
    background: var(--white);
    font-family: "Open Sans", Arial, sans-serif;
    color: var(--ink);
  }
  .abs { position: absolute; }

  /* header */
  .utility-bar { left: 0; top: 0; width: 675px; height: 18px; background: var(--rose); }
  .utility-links { right: 95px; top: 4px; display: flex; gap: 6px; font-size: 6px; color: var(--white); text-transform: uppercase; }
  .main-nav { left: 0; top: 18px; width: 675px; height: 42px; background: var(--peach); }
  .nav-links { left: 366px; top: 18px; height: 42px; display: flex; font-size: 7.5px; text-transform: uppercase; color: #5a3b38; }
  .nav-links span { display: flex; align-items: center; padding: 0 5px; height: 100%; }
  .nav-links .active { background: var(--rose); color: var(--white); padding: 0 8px; }
  .brand-badge {
    left: 91px; top: -28px; width: 130px; height: 130px; border-radius: 50%; z-index: 10;
    background: var(--white); box-shadow: 0 2px 6px rgba(0,0,0,.25);
    display: flex; align-items: flex-end; justify-content: center; padding-bottom: 34px;
  }
  .brand-name { font-size: 17px; font-weight: 400; color: #a98a86; letter-spacing: 1px; }

  /* hero */
  .hero-sides { left: 0; top: 60px; width: 675px; height: 225px; background: radial-gradient(circle at 20% 30%, #ee7a98, var(--rose-deep) 70%); }
  .hero-photo { left: 87px; top: 60px; width: 500px; height: 225px; background: linear-gradient(100deg, #d9a08f 0%, #f1d0c6 35%, #f6e6ef 60%, #eec6da 100%); }
  .hero-arrow { top: 140px; }
  .hero-caption { left: 306px; top: 114px; width: 272px; height: 40px; background: rgba(150,40,75,.75); border-radius: 3px; color: var(--white); font-size: 17px; display: flex; align-items: center; justify-content: center; }
  .hero-sub { left: 306px; top: 168px; width: 272px; text-align: center; font-size: 13px; color: var(--wine); }
  .hero-cta { left: 379px; top: 205px; width: 117px; height: 28px; background: var(--rose-dark); border-radius: 2px; color: var(--white); font-size: 11.5px; display: flex; align-items: center; justify-content: center; }
  .hero-fade { left: 0; top: 285px; width: 675px; height: 65px; background: linear-gradient(#f7c8d3, var(--white)); }

  /* section titles */
  .section-banner { left: 157px; top: 327px; width: 358px; height: 40px; background: linear-gradient(90deg, rgba(247,190,205,0), #f6b4c5 25%, #f6b4c5 75%, rgba(247,190,205,0)); border-radius: 20px; }
  .section-title { font-family: "Courgette", cursive; font-weight: 400; color: var(--rose-dark); font-size: 15px; width: 675px; left: 0; text-align: center; }

  /* package cards */
  .package-card { top: 383px; width: 108px; height: 223px; }
  .package-card .panel { position: absolute; left: 0; top: 50px; width: 108px; height: 173px; background: var(--rose); border-radius: 2px; }
  .package-card .photo { position: absolute; left: 0; top: 0; width: 108px; height: 108px; border-radius: 50%; }
  .package-card .name { position: absolute; top: 120px; width: 108px; text-align: center; font-size: 8.5px; color: var(--white); text-transform: uppercase; }
  .package-card .rule { position: absolute; left: 16px; top: 140px; width: 76px; height: 1px; background: rgba(255,255,255,.6); }
  .package-card .desc { position: absolute; left: 6px; top: 148px; width: 96px; text-align: center; font-size: 6.5px; line-height: 12.5px; color: var(--white); }
  .package-card .price { position: absolute; left: 17px; top: 198px; width: 74px; height: 15px; background: var(--white); border-radius: 2px; font-size: 8px; font-weight: 700; color: var(--wine); display: flex; align-items: center; justify-content: center; }

  /* product list */
  .product { top: 699px; width: 90px; text-align: center; }
  .product svg { display: block; margin: 0 auto; }
  .product .name { margin-top: 8px; font-size: 7.5px; color: var(--hex-red); }
  .product .desc { margin-top: 6px; font-size: 6.8px; line-height: 11px; color: var(--ink); }
  .product .more { margin: 10px auto 0; width: 63px; height: 15px; background: var(--blush); font-size: 6px; display: flex; align-items: center; justify-content: center; color: var(--ink); }

  /* booking */
  .booking { left: 88px; top: 887px; width: 500px; height: 185px; border-radius: 5px; overflow: hidden; background: linear-gradient(90deg, #f0b12e 0%, #f4d08a 30%, #f5ded4 55%, #bfe0ee 100%); }
  .booking-title { left: 103px; top: 914px; font-family: "Oswald", sans-serif; font-weight: 300; font-size: 34px; line-height: 42px; color: var(--white); text-shadow: 0 1px 3px rgba(0,0,0,.35); text-transform: uppercase; }
  .field { background: rgba(255,255,255,.88); border-radius: 3px; font-size: 10px; color: #b4323b; padding: 6px 8px; }
  .submit { left: 367px; top: 1032px; width: 173px; height: 26px; background: var(--red); color: var(--white); font-size: 10.5px; display: flex; align-items: center; justify-content: center; border-radius: 2px; }

  /* footer */
  .site-footer { left: 0; top: 1088px; width: 675px; height: 112px; background: linear-gradient(90deg, #1a1a1a, #2c2c2c 50%, #1a1a1a); }
  .footer-brand { left: 88px; top: 1148px; width: 120px; text-align: center; font-size: 16px; color: #cdbcb8; letter-spacing: 1px; }
  .footer-divider { left: 208px; top: 1108px; height: 76px; border-left: 1px dashed #6a3a45; }
  .footer-address { left: 222px; top: 1108px; font-size: 6.3px; line-height: 12.5px; color: #d8d8d8; }
  .footer-address h4 { font-weight: 400; color: var(--rose); font-size: 6.5px; margin-bottom: 1px; text-transform: uppercase; }
  .footer-address .row { display: flex; align-items: center; gap: 4px; }
  .footer-links { right: 97px; top: 1112px; font-size: 6.3px; color: var(--footer-text); }
  .social { left: 493px; top: 1134px; display: flex; gap: 4px; }
  .social span { width: 14px; height: 14px; border-radius: 50%; background: var(--rose); }
  .copyright { right: 97px; top: 1161px; font-size: 6px; color: #d8d8d8; }
</style>
</head>
<body>

<header>
  <div class="abs utility-bar"></div>
  <nav class="abs utility-links"><span>My Account</span><span>Checkout</span><span>Shop</span><span>Cart (0)</span></nav>
  <div class="abs main-nav"></div>
  <nav class="abs nav-links">
    <span class="active">Home</span><span>About Us</span><span>Product</span><span>Packages</span><span>Contact</span>
  </nav>
  <div class="abs brand-badge"><span class="brand-name">MossVane</span></div>
</header>

<section class="hero">
  <div class="abs hero-sides" role="img" aria-label="Soft pink bokeh backdrop"></div>
  <div class="abs hero-photo" role="img" aria-label="Close-up beauty photograph of a woman with eyes closed beside blossoms"></div>
  <svg class="abs hero-arrow" style="left:88px" width="14" height="44" viewBox="0 0 14 44"><path d="M12 2 L2 22 L12 42" fill="none" stroke="#fff" stroke-width="1.2" opacity=".8"/></svg>
  <svg class="abs hero-arrow" style="left:573px" width="14" height="44" viewBox="0 0 14 44"><path d="M2 2 L12 22 L2 42" fill="none" stroke="#fff" stroke-width="1.2" opacity=".8"/></svg>
  <div class="abs hero-caption">LOREM IPSUM DOLOR</div>
  <p class="abs hero-sub">lorem ipsum dolor sit is dummy text</p>
  <div class="abs hero-cta">JOIN NOW</div>
  <div class="abs hero-fade"></div>
</section>

<section class="packages">
  <div class="abs section-banner" role="img" aria-label="Soft pink brushed ribbon banner"></div>
  <h2 class="abs section-title" style="top:336px">Our Packages</h2>

  <article class="abs package-card" style="left:87px">
    <div class="panel"></div>
    <div class="photo" style="background:radial-gradient(circle at 40% 40%, #d9d3d6, #7d6c78 70%, #3b2e36)" role="img" aria-label="Portrait of a woman with flowers, view detail overlay"></div>
    <div class="abs" style="left:0;top:46px;width:108px;text-align:center;font-size:7px;color:#111">VIEW DETAIL</div>
    <div class="name">Product Name</div><div class="rule"></div>
    <p class="desc">Lorem ipsum dolor sit amet adipiscing elit, sed diam nonummy nibh euismod</p>
    <div class="price">$ 100.00</div>
  </article>
  <article class="abs package-card" style="left:219px">
    <div class="panel"></div>
    <div class="photo" style="background:radial-gradient(circle, #f6d8bf 30%, #8aa04a 75%, #6b3a2c)" role="img" aria-label="Jar of cream with fruit and leaves"></div>
    <div class="name">Product Name</div><div class="rule"></div>
    <p class="desc">Lorem ipsum dolor sit amet adipiscing elit, sed diam nonummy nibh euismod</p>
    <div class="price">$ 100.00</div>
  </article>
  <article class="abs package-card" style="left:350px">
    <div class="panel"></div>
    <div class="photo" style="background:radial-gradient(circle at 55% 45%, #e2b8a0, #8a5a44 65%, #3a2620)" role="img" aria-label="Vintage styled portrait with pearls"></div>
    <div class="name">Product Name</div><div class="rule"></div>
    <p class="desc">Lorem ipsum dolor sit amet adipiscing elit, sed diam nonummy nibh euismod</p>
    <div class="price">$ 100.00</div>
  </article>
  <article class="abs package-card" style="left:479px">
    <div class="panel"></div>
    <div class="photo" style="background:linear-gradient(#bfe4f2, #efd3c4 55%, #3d6fa0)" role="img" aria-label="Woman relaxing on spa towels"></div>
    <div class="name">Product Name</div><div class="rule"></div>
    <p class="desc">Lorem ipsum dolor sit amet adipiscing elit, sed diam nonummy nibh euismod</p>
    <div class="price">$ 100.00</div>
  </article>
</section>

<section class="products">
  <h2 class="abs section-title" style="top:657px">Our Product</h2>

  <article class="abs product" style="left:92px">
    <svg width="77" height="67" viewBox="0 0 77 67" role="img" aria-label="Heart shaped blush compact"><polygon points="19,1 58,1 76,33.5 58,66 19,66 1,33.5" fill="#f7e3d8" stroke="#c9343e" stroke-width="1.5"/></svg>
    <div class="name">Product Name</div>
    <p class="desc">Lorem ipsum dolor sit amet adipiscing elit. sed diam nonummy nibh</p>
    <div class="more">[ view detail ]</div>
  </article>
  <article class="abs product" style="left:192px">
    <svg width="77" height="67" viewBox="0 0 77 67" role="img" aria-label="Cream jar with fruit"><polygon points="19,1 58,1 76,33.5 58,66 19,66 1,33.5" fill="#f0cfae" stroke="#c9343e" stroke-width="1.5"/></svg>
    <div class="name">Product Name</div>
    <p class="desc">Lorem ipsum dolor sit amet adipiscing elit. sed diam nonummy nibh</p>
    <div class="more">[ view detail ]</div>
  </article>
  <article class="abs product" style="left:292px">
    <svg width="77" height="67" viewBox="0 0 77 67" role="img" aria-label="Skincare bottles and tubes"><polygon points="19,1 58,1 76,33.5 58,66 19,66 1,33.5" fill="#e9d6c2" stroke="#c9343e" stroke-width="1.5"/></svg>
    <div class="name">Product Name</div>
    <p class="desc">Lorem ipsum dolor sit amet adipiscing elit. sed diam nonummy nibh</p>
    <div class="more">[ view detail ]</div>
  </article>
  <article class="abs product" style="left:392px">
    <svg width="77" height="67" viewBox="0 0 77 67" role="img" aria-label="Cosmetic tubes with greenery"><polygon points="19,1 58,1 76,33.5 58,66 19,66 1,33.5" fill="#c9c3d6" stroke="#c9343e" stroke-width="1.5"/></svg>
    <div class="name">Product Name</div>
    <p class="desc">Lorem ipsum dolor sit amet adipiscing elit. sed diam nonummy nibh</p>
    <div class="more">[ view detail ]</div>
  </article>
  <article class="abs product" style="left:492px">
    <svg width="77" height="67" viewBox="0 0 77 67" role="img" aria-label="Lipstick and nail polish set"><polygon points="19,1 58,1 76,33.5 58,66 19,66 1,33.5" fill="#e8c4c8" stroke="#c9343e" stroke-width="1.5"/></svg>
    <div class="name">Product Name</div>
    <p class="desc">Lorem ipsum dolor sit amet adipiscing elit. sed diam nonummy nibh</p>
    <div class="more">[ view detail ]</div>
  </article>
</section>

<section class="booking-section">
  <div class="abs booking" role="img" aria-label="Woman resting during a spa treatment with a flower"></div>
  <h2 class="abs booking-title">Booking for<br>Spa Treatment<br>and Packages</h2>
  <div class="abs field" style="left:322px;top:921px;width:122px;height:26px">Name</div>
  <div class="abs field" style="left:449px;top:921px;width:123px;height:26px">Email</div>
  <div class="abs field" style="left:322px;top:952px;width:250px;height:70px">Notes</div>
  <div class="abs submit">SUBMIT</div>
</section>

<footer>
  <div class="abs site-footer"></div>
  <div class="abs footer-brand">MossVane</div>
  <div class="abs footer-divider"></div>
  <div class="abs footer-address">
    <h4>Address</h4>
    Lorem Ipsum has been the<br>industry's standard dummy text<br>the industry's standard dummy text
    <div class="row" style="margin-top:2px">
      <svg width="8" height="8" viewBox="0 0 8 8"><path d="M1.5 0.5 L3 0.5 L3.6 2.3 L2.6 3 Q3.3 4.6 5 5.4 L5.7 4.4 L7.5 5 L7.5 6.5 Q4 7.5 1.5 5 Q-0.5 2.5 1.5 0.5Z" fill="#fff"/></svg>1111 1111
    </div>
    <div class="row">
      <svg width="8" height="6" viewBox="0 0 8 6"><rect x=".5" y=".5" width="7" height="5" fill="none" stroke="#fff" stroke-width=".8"/><path d="M.5 .5 L4 3.3 L7.5 .5" fill="none" stroke="#fff" stroke-width=".8"/></svg>test@mossvane.com
    </div>
  </div>
  <nav class="abs footer-links">Home • About us • Services • Packages • Contact Us</nav>
  <div class="abs social" aria-label="Social links"><span></span><span></span><span></span><span></span><span></span></div>
  <p class="abs copyright">Design © 2014. All Rights Reserved.</p>
</footer>

</body>
</html>
```